Company or website name
- Fernhollow Plank Co. Newsletter
- We sell butcher blocks, butcher block counters, butcher block tables, butcher block cutting boards, and other gourmet kitchen items.

```html
<!DOCTYPE html>
<html lang="en">
<head>
<meta charset="utf-8">
<title>Fernhollow Plank Co. Newsletter</title>
<link href="https://fonts.googleapis.com/css2?family=Righteous&family=Open+Sans:wght@400&family=Roboto+Condensed:wght@700&display=swap" rel="stylesheet">
<style>
:root{
  --blue:#4f7596;
  --blue-soft:#b9cadd;
  --yellow:#fbc44f;
  --yellow-pale:#fdf0c4;
  --orange:#f3a94a;
  --ink:#3a3a3a;
  --caption:#3f4f60;
  --white:#ffffff;
}
*{margin:0;padding:0;box-sizing:border-box}
html,body{width:927px;height:1200px;overflow:hidden;background:var(--white)}
.page{position:relative;width:927px;height:1200px;overflow:hidden;background:var(--white);font-family:"Open Sans",Arial,sans-serif;color:var(--ink)}

.masthead-name{position:absolute;left:56px;top:72px;font-family:"Righteous",Arial,sans-serif;font-size:30px;letter-spacing:9px;color:var(--blue);text-transform:uppercase;white-space:nowrap;line-height:1}
.masthead-band{position:absolute;left:39px;top:105px;width:888px;height:31px;background:linear-gradient(90deg,var(--orange),var(--yellow) 30%,#f6b563 55%,var(--yellow) 75%,#d9b264)}
.masthead-info{position:absolute;left:54px;top:141px;font-family:"Righteous",Arial,sans-serif;font-size:10.5px;letter-spacing:2.4px;color:var(--blue);text-transform:uppercase;white-space:nowrap}
.issue{position:absolute;right:56px;top:141px;font-family:"Righteous",Arial,sans-serif;font-size:10.5px;letter-spacing:3px;color:var(--blue)}

.side-band{position:absolute;left:0;top:165px;width:133px;height:1035px;background:var(--yellow-pale)}
.side-title{position:absolute;left:38px;top:1192px;transform-origin:0 0;transform:rotate(-90deg);font-family:"Righteous",Arial,sans-serif;font-size:102px;line-height:100px;color:var(--yellow);white-space:nowrap}

.headline{font-family:"Righteous",Arial,sans-serif;color:var(--blue);font-size:20px;line-height:23px;text-transform:lowercase;white-space:nowrap}
.body-copy{font-size:15.2px;line-height:22.6px;color:var(--ink);white-space:nowrap}
.end-mark{display:inline-block;width:8px;height:14px;background:var(--yellow);vertical-align:-1px;margin-left:4px}

.story-main{position:absolute;left:169px;top:194px}
.story-main .body-copy{margin-top:12px}
.story-cont{position:absolute;left:541px;top:627px}
.story-second{position:absolute;left:169px;top:1012px}
.story-second .headline{font-size:21px}
.story-second .body-copy{margin-top:6px}

.photo-table{position:absolute;left:505px;top:156px;width:380px;height:468px;background:linear-gradient(180deg,#f6f4f1 0%,#d98a3c 22%,#c5712a 35%,#2a2624 48%,#1c1a19 70%,#f4f3f1 82%,#f4f3f1 100%)}
.photo-caption{position:absolute;left:620px;top:547px;width:265px;text-align:center;font-family:"Roboto Condensed",Arial,sans-serif;font-weight:700;font-size:12.3px;line-height:19px;color:var(--caption);white-space:nowrap}

.divider{position:absolute;left:521px;top:624px;width:1px;height:576px;background:var(--blue)}

.photo-board{position:absolute;left:142px;top:750px;width:300px;height:220px;border-radius:60px/50px;transform:rotate(12deg);background:radial-gradient(ellipse at 40% 40%,#e0b584,#c98f57 70%,#a86a38);box-shadow:6px 10px 14px rgba(0,0,0,.35)}
.callout{position:absolute;left:334px;top:679px;width:178px;height:107px;border-radius:50%;background:var(--blue);color:var(--white);font-family:"Roboto Condensed",Arial,sans-serif;font-weight:700;font-size:12px;line-height:19.5px;text-align:center;padding-top:14px;white-space:nowrap}

.spot-area{position:absolute;left:521px;top:871px;width:350px;height:212px;background:linear-gradient(180deg,var(--blue-soft),#c4d2e2)}
.spot-caption{position:absolute;left:543px;top:1090px;font-family:"Roboto Condensed",Arial,sans-serif;font-weight:700;font-size:12.6px;line-height:19.5px;color:var(--ink);white-space:nowrap}
</style>
</head>
<body>
<div class="page">
  <div class="masthead-name">Fernhollow Plank Co.</div>
  <div class="masthead-band" role="img" aria-label="Decorative band of warm yellow and orange blocks"></div>
  <div class="masthead-info">PO Box 48210 ~ Tacoma ~ WA 98402 ~ www.fernhollowplank.com</div>
  <div class="issue">VOL. 1</div>

  <div class="side-band"></div>
  <div class="side-title">feature of the month</div>

  <div class="photo-table" role="img" aria-label="Photograph of an end-grain butcher block kitchen table with black legs, wicker drawers, wine bottles and glasses on top"></div>
  <div class="photo-caption">Lorem ipsum olore eu feugiat nulla facilisis<br>at vero eros et accumsan et iusto odio di</div>

  <article class="story-main">
    <h2 class="headline">Lorem ipsum olore eu feugiat<br>nulla facilisis at ver accu</h2>
    <p class="body-copy">msan et iusto odio dignissim qui<br>blandit praesent al aliquip ex ea<br>exercitation commodo consequat.<br>Utwisi enim ad minim veniam,<br>quis nostrud exerci tation ullam.<br>Duis autem vel eum iriure dolor in<br>hendrerit invu lutate velit esse molstie<br>consequat, vel illum dolore eu feugiat.<br>Nulla facilisis at vero eros et accums an<br>et iusto odio dignissim. Suscipit lobortis<br>nisl ut aliquip ex eum iriure dolor in<br>hendreritea quis nostrud exerci. Ut wisi<br>enim ad minim veniam, quis nostrud<br>exerci tation ullam corper suscipit lobortis<br>nisl ut aliquip ex ea commodo cons equat.<br>Vblandit praesent luptatum zzril delenit<br>augue duis dolore te feugait nulla. Duis<br>autem vel eum iriure dolor in hendrerit<br>in vulputate velit esse<br>molestie conse<span class="end-mark"></span></p>
  </article>

  <div class="divider"></div>

  <div class="story-cont">
    <p class="body-copy">dolor in hendrerit in vulputate velit esse<br>molestie consequat.Vel facilisis at vero eros<br>illum dolore eu feugiat nulla facilisis at vero<br>eros et accumsan et iusto odiodignissim<br>qui blandit praesent luptatum&nbsp; facilisis at<br>vero eroszzril delenit augue duis dolore<br>te feugait nulla facilisi.Wisi enim ad Duis<br>autem vel eum iriure dolor in hendrerit in<br>vulputate velit esse molestie consequat, vel<br>illum dolore eu feugiat nulla facilisi<span class="end-mark"></span></p>
  </div>

  <div class="photo-board" role="img" aria-label="Photograph of a wooden carving board with a juice groove"></div>
  <div class="callout">Lorem ipsum olore<br>eu feugiat nulla facilisis at<br>vero eros et accumsan et iusto<br>odio di</div>

  <article class="story-second">
    <h2 class="headline">quat, vel illum dolore eu feugi</h2>
    <p class="body-copy">at. Ut wisi enim ad minim veniam, quis<br>nostrud exerci tation ullamcorper suscipit<br>lobortis nisl ut aliquip ex ea commodo<br>consequat.&nbsp; Duis autem vel eum iriure</p>
  </article>

  <div class="spot-area" role="img" aria-label="Blue-tinted photograph of a cleaver resting on a round chopping block"></div>
  <p class="spot-caption">A chart or photograph for this area - or, perhaps a small spot<br>cartoon, featured fact or quote, the latest innovation or<br>upcoming item.</p>
</div>
</body>
</html>
```